Business Card Kelda Law llc examples and ideas are attached.

in addition to the logo we need a desription what we do: "Reprsenting students with disabilites obtain services to progress in the public school system."

If you can squeeze it on the fron at the bottom great if not put it on the back

```html
<!DOCTYPE html>
<html lang="en">
<head>
<meta charset="utf-8">
<title>Kelda Law llc – Business Card</title>
<link rel="stylesheet" href="https://fonts.googleapis.com/css2?family=Cinzel:wght@600&family=Open+Sans:wght@400;700&display=swap">
<style>
  :root {
    --navy: #0d2140;
    --navy-deep: #071630;
    --navy-soft: #1a3154;
    --gold: #c9a13c;
    --gold-light: #e3c46a;
    --white: #ffffff;
    --ink: #17294a;
    --mist: #c9d2de;
    --backdrop: #ece9e4;
  }
  * { margin: 0; padding: 0; box-sizing: border-box; }
  html, body {
    width: 1200px; height: 800px; overflow: hidden;
    background: var(--backdrop);
  }
  .stage {
    width: 1200px; height: 800px;
    display: flex; align-items: center; justify-content: center; gap: 40px;
  }
  .card {
    position: relative;
    width: 540px; height: 309px;
    overflow: hidden;
    border-radius: 4px;
    box-shadow: 0 8px 24px rgba(0,0,0,.18);
  }

  /* Back of card */
  .card-back {
    background: radial-gradient(ellipse at 50% 35%, var(--navy-soft) 0%, var(--navy) 55%, var(--navy-deep) 100%);
    display: flex; flex-direction: column; align-items: center;
  }
  .back-mark {
    margin-top: 58px;
    width: 58px; height: 58px;
    background: var(--gold);
  }
  .back-name {
    margin-top: 16px;
    font-family: "Cinzel", serif; font-weight: 600;
    font-size: 30px; color: var(--gold-light);
    letter-spacing: .5px;
  }
  .back-tagline {
    margin-top: 36px;
    font-family: "Open Sans", sans-serif; font-weight: 400;
    font-size: 11.5px; line-height: 17px;
    letter-spacing: 1.6px; text-transform: uppercase;
    color: var(--mist); text-align: center;
  }

  /* Front of card */
  .card-front { background: var(--white); }
  .front-bg { position: absolute; inset: 0; }
  .front-brand {
    position: absolute; left: 30px; top: 40px;
    display: flex; align-items: center; gap: 16px;
  }
  .front-mark {
    width: 64px; height: 64px;
    background: var(--navy);
  }
  .front-name {
    font-family: "Cinzel", serif; font-weight: 600;
    font-size: 28px; color: var(--navy);
  }
  .attorney {
    position: absolute; right: 28px; top: 34px; text-align: right;
    font-family: "Open Sans", sans-serif;
  }
  .attorney-name { font-weight: 700; font-size: 17px; color: var(--gold); }
  .attorney-title { font-size: 11px; color: var(--ink); margin-top: -2px; }
  .contact {
    position: absolute; left: 30px; top: 178px;
    font-family: "Open Sans", sans-serif; font-size: 12.5px; line-height: 17px;
    color: var(--white);
    list-style: none;
  }
  .contact-item { display: flex; gap: 8px; align-items: flex-start; }
  .contact-item + .contact-item { margin-top: 6px; }
  .contact-icon { width: 13px; height: 13px; margin-top: 2px; flex: none; fill: var(--gold); }
</style>
</head>
<body>
<main class="stage">

  <section class="card card-back" aria-label="Card back">
    <div class="back-mark" aria-hidden="true"></div>
    <p class="back-name">Kelda Law llc</p>
    <p class="back-tagline">Reprsenting students with disabilites<br>obtain services to progress in the public school system</p>
  </section>

  <section class="card card-front" aria-label="Card front">
    <svg class="front-bg" viewBox="0 0 540 309" preserveAspectRatio="none" aria-hidden="true">
      <polygon points="0,138 540,150 540,157 0,145" fill="var(--gold)"/>
      <polygon points="0,145 540,157 540,309 0,309" fill="var(--navy)"/>
    </svg>

    <div class="front-brand">
      <div class="front-mark" aria-hidden="true"></div>
      <p class="front-name">Kelda Law llc</p>
    </div>

    <div class="attorney">
      <p class="attorney-name">Dana R Kelda</p>
      <p class="attorney-title">Attorney at Law</p>
    </div>

    <ul class="contact">
      <li class="contact-item">
        <svg class="contact-icon" viewBox="0 0 16 16" aria-hidden="true"><path d="M8 0a5.5 5.5 0 0 0-5.5 5.5C2.5 10 8 16 8 16s5.5-6 5.5-10.5A5.5 5.5 0 0 0 8 0zm0 8a2.5 2.5 0 1 1 0-5 2.5 2.5 0 0 1 0 5z"/></svg>
        <span>1450 Ne 18th Ave<br>Fort Lauderdale FL33305<br>By appointment only</span>
      </li>
      <li class="contact-item">
        <svg class="contact-icon" viewBox="0 0 16 16" aria-hidden="true"><path d="M3.6 1 6 3.8 4.6 5.6a9 9 0 0 0 5.8 5.8L12.2 10l2.8 2.4-1.6 2.4C7 14.4 1.6 9 1.2 2.6z"/></svg>
        <span>813 555 0192</span>
      </li>
      <li class="contact-item">
        <svg class="contact-icon" viewBox="0 0 16 16" aria-hidden="true"><path d="M1 3h14v10H1zm1.5 1.2L8 8.5l5.5-4.3z"/></svg>
        <span>dana.keldalaw@example.com</span>
      </li>
    </ul>
  </section>

</main>
</body>
</html>
```